Reed & Vale NC grand opening (for BILLBOARD)

Advertising the grand opening of our cannabis/hemp shop in NC. We will sell all things hemp (flower, cartridges, disposables, edibles, creams, lotions, pet products etc...)

Requirements
Must have
• include, open starting Aug 1, but grand opening Aug 15th.
Nice to have
• Difference slogan ideas "Save some cash, buy our grass" "Find your perfect high at Reed & Vale cannabis store" "Experience Nature's Gift: Reed & Vale Cannabis Store"

```html
<!DOCTYPE html>
<html lang="en">
<head>
<meta charset="utf-8">
<title>Reed &amp; Vale Billboard</title>
<link rel="stylesheet" href="https://fonts.googleapis.com/css2?family=Bebas+Neue&display=swap">
<style>
  :root {
    --page-bg: #b4b3b3;
    --leaf-green: #7dc142;
    --forest-green: #1e6a36;
    --ink-navy: #13103a;
    --paper: #ffffff;
  }
  html, body {
    margin: 0;
    padding: 0;
    width: 1200px;
    height: 1200px;
    overflow: hidden;
    background: var(--page-bg);
  }
  .canvas {
    position: relative;
    width: 1200px;
    height: 1200px;
  }
  .billboard {
    position: absolute;
    left: 40px;
    top: 436px;
    width: 1120px;
    height: 328px;
    box-shadow: 2px 3px 4px rgba(0, 0, 0, 0.25);
    background: var(--paper);
  }
  .billboard svg {
    display: block;
    width: 100%;
    height: 100%;
  }
  .headline,
  .directions,
  .brand-name,
  .opening-dates {
    font-family: "Bebas Neue", "Oswald", sans-serif;
  }
  .headline--dark { fill: var(--ink-navy); }
  .headline--light { fill: var(--paper); }
  .directions { fill: var(--paper); }
  .brand-name { fill: var(--ink-navy); }
  .opening-dates { fill: var(--forest-green); }
  .panel-green { fill: var(--leaf-green); }
  .panel-navy { fill: var(--ink-navy); }
  .swoosh-navy { fill: var(--ink-navy); }
  .swoosh-green { fill: var(--forest-green); }
  .billboard-bg { fill: var(--paper); }
</style>
</head>
<body>
<main class="canvas">
  <section class="billboard" aria-label="Reed &amp; Vale billboard">
    <svg viewBox="0 0 1292 378" preserveAspectRatio="none" xmlns="http://www.w3.org/2000/svg">
      <rect class="billboard-bg" x="0" y="0" width="1292" height="378"/>

      <path class="panel-green" d="M0 0 H770 C722 38 694 96 702 150 C710 205 734 240 738 272 H0 Z"/>
      <path class="panel-navy" d="M0 272 H738 C744 318 746 352 730 378 H0 Z"/>

      <path class="swoosh-navy" d="M770 0 C722 38 694 96 702 150 C710 205 734 240 738 272 C744 318 746 352 730 378 L742 378 C770 345 770 300 756 250 C742 205 714 160 718 120 C722 70 748 30 784 0 Z"/>
      <path class="swoosh-green" d="M800 0 C752 42 728 102 738 158 C748 212 784 250 792 306 C806 252 778 212 764 160 C752 108 764 48 814 0 Z"/>

      <text class="headline headline--dark" x="33" y="140" font-size="122" textLength="641" lengthAdjust="spacingAndGlyphs">SAVE SOME CASH</text>
      <text class="headline headline--light" x="33" y="250" font-size="122" textLength="641" lengthAdjust="spacingAndGlyphs">BUY OUR GRASS</text>
      <text class="directions" x="33" y="345" font-size="68" textLength="620" lengthAdjust="spacingAndGlyphs">OFF EXIT 4B ASHGROVE RD</text>

      <text class="brand-name" x="1030" y="212" font-size="112" text-anchor="middle">Reed &amp; Vale</text>
      <text class="opening-dates" x="1030" y="280" font-size="40" text-anchor="middle" textLength="420" lengthAdjust="spacingAndGlyphs">OPEN AUG 1 &#8226; GRAND OPENING AUG 15</text>
    </svg>
  </section>
</main>
</body>
</html>
```